Web Design Project - Dating and Social Networking Site for Artists

Hello,
Need a homepage design for Travolia.net, an existing dating and networking site for artists. The theme for this site is: "Find or serve as a Muse." Greek God and Goddess (Muse) theme is welcome, but not required. Website is geared toward 20 - 45 year old individuals. Existing background colors are blue, green and white. Nothing too slick, cheesy or serious. The final design should communicate uniqueness, romance and excitement. Playful is good too!
Dating

```html
<!DOCTYPE html>
<html lang="en">
<head>
<meta charset="utf-8">
<title>Travolia.net – Find or serve as a Muse</title>
<link rel="stylesheet" href="https://fonts.googleapis.com/css2?family=PT+Sans:wght@400;700&family=PT+Sans+Narrow:wght@400;700&family=Roboto:wght@400;500&display=swap">
<style>
:root{
  --teal-dark:#0b6b5a;
  --teal:#137a6a;
  --cyan:#1aa3cf;
  --cyan-light:#3fc6e8;
  --sky-top:#1a8fd0;
  --sky-bottom:#7ff6fb;
  --panel:#2f6478;
  --panel-foot:#6d7a80;
  --orange:#f06a0f;
  --orange-light:#ff8a2a;
  --ink:#222;
  --ink-soft:#444;
  --rule:#d6d6d6;
  --green-link:#2ecc3c;
  --white:#fff;
}
*{box-sizing:border-box;margin:0;padding:0}
html,body{width:1200px;height:1100px;overflow:hidden;background:var(--white)}
body{font-family:"Roboto",Arial,sans-serif;color:var(--ink)}
.page{position:relative;width:1200px;height:1100px;overflow:hidden}

/* header */
.site-header{position:absolute;left:0;top:0;width:1200px;height:115px;background:var(--white)}
.brand{position:absolute;left:200px;top:44px;display:flex;align-items:center;gap:8px;
  font-family:"PT Sans",sans-serif;font-weight:700;font-size:34px;color:var(--teal-dark);letter-spacing:-.5px}
.brand-mark{width:14px;height:14px;background:var(--cyan)}
.account{position:absolute;top:7px;left:843px;display:flex;gap:7px}
.account a{display:block;width:72px;height:27px;line-height:27px;text-align:center;border-radius:2px;
  font-family:"PT Sans",sans-serif;font-size:14px;color:var(--white);text-decoration:none}
.btn-login{background:var(--teal-dark)}
.btn-signup{background:var(--cyan)}
.main-nav{position:absolute;top:76px;left:537px;display:flex;gap:0}
.main-nav a{font-family:"PT Sans",sans-serif;font-size:12px;color:var(--ink);text-decoration:none;margin-right:25px}
.main-nav a.is-current{color:var(--cyan)}
.main-nav a:last-child{margin-right:0}

/* hero */
.hero{position:absolute;left:0;top:115px;width:1200px;height:445px;
  background:linear-gradient(180deg,var(--sky-top) 0%,#3db5ec 35%,#5fd9f5 70%,var(--sky-bottom) 100%)}
.hero-title{position:absolute;left:0;width:1200px;top:33px;text-align:center;
  font-family:"PT Sans",sans-serif;font-size:35px;color:var(--white);font-weight:400;text-shadow:0 1px 3px rgba(0,0,0,.25)}
.hero-sub{position:absolute;left:0;width:1200px;top:84px;text-align:center;
  font-family:"PT Sans",sans-serif;font-size:12px;color:var(--white)}
.hero-sub a{color:var(--green-link);text-decoration:none;margin-left:4px}

.photo{position:absolute;background:linear-gradient(135deg,#c99a78,#e8c9ae 55%,#8a7060)}
.photo.cool{background:linear-gradient(135deg,#9bb8cc,#e6d2bf 55%,#6a5a52)}
.photo.warm{background:linear-gradient(135deg,#d8b48c,#f1dcc4 50%,#a07a5a)}

/* join panel */
.join{position:absolute;left:200px;top:237px;width:238px;height:338px;border-radius:4px 4px 0 0;
  background:linear-gradient(180deg,#2e6a6e 0%,var(--panel) 40%,#3b6e86 100%);box-shadow:0 6px 8px rgba(0,0,0,.25)}
.join-head{height:46px;background:var(--teal-dark);border-radius:4px 4px 0 0;
  font-family:"PT Sans Narrow",sans-serif;font-weight:700;font-size:24px;color:var(--white);padding:8px 0 0 17px}
.join-head span{color:var(--cyan-light)}
.join-foot{position:absolute;left:0;bottom:0;width:238px;height:20px;background:var(--panel-foot)}
.field-label{position:absolute;font-family:"PT Sans",sans-serif;font-size:12px;color:var(--white)}
.box{position:absolute;height:20px;background:var(--white);border:1px solid #aaa;
  font-family:"Roboto",sans-serif;font-size:11px;color:var(--ink);line-height:18px;padding-left:6px}
.box.select::after{content:"";position:absolute;right:5px;top:7px;border-left:4px solid transparent;border-right:4px solid transparent;border-top:5px solid #222}
.btn-match{position:absolute;left:48px;top:286px;width:145px;height:33px;border-radius:3px;
  background:linear-gradient(180deg,var(--orange-light),var(--orange));
  font-family:"PT Sans",sans-serif;font-size:16px;color:var(--white);text-align:center;line-height:33px}

/* content */
.welcome{position:absolute;left:200px;top:612px;width:500px}
.section-title{font-family:"PT Sans",sans-serif;font-size:17px;font-weight:700;color:#333;text-transform:uppercase}
.section-title span{color:var(--cyan)}
.welcome p{margin-top:14px;font-size:10px;line-height:20.8px;color:var(--ink-soft)}
.read-more{position:absolute;top:199px;left:0;font-family:"PT Sans",sans-serif;font-size:10px;font-weight:700;color:var(--teal);text-decoration:none}
.divider-v{position:absolute;left:713px;top:625px;width:1px;height:135px;background:linear-gradient(180deg,transparent,#e6e6e6,transparent)}

.members{position:absolute;left:742px;top:612px;width:252px}
.member{position:absolute;width:57px;text-align:center}
.member .face{width:57px;height:69px;background:linear-gradient(160deg,#8a9aa8,#d9b9a0 60%,#5b4a42)}
.member span{display:block;font-family:"PT Sans",sans-serif;font-size:9px;font-weight:700;color:var(--cyan);margin-top:1px}

/* footer */
.rule{position:absolute;left:200px;width:793px;height:2px;background:var(--rule)}
.footer-nav{position:absolute;left:200px;top:868px;width:793px;display:flex;justify-content:space-between}
.footer-nav a{font-family:"PT Sans",sans-serif;font-size:12px;color:var(--ink);text-decoration:none}
.footer-copy{position:absolute;left:200px;top:907px;width:675px;font-size:10px;line-height:17.5px;color:var(--ink)}
.badge{position:absolute;left:888px;top:912px;width:105px;height:41px;border-radius:4px;background:#1f5e8c}
.footer-brand{position:absolute;left:200px;top:1025px;display:flex;align-items:center;gap:7px;
  font-family:"PT Sans",sans-serif;font-weight:700;font-size:26px;color:#333}
.footer-brand i{display:block;width:11px;height:11px;background:#555}
.copyright{position:absolute;left:545px;top:1048px;font-size:10px;color:var(--ink)}
.social{position:absolute;top:1036px;display:flex;gap:0}
.social span{display:block;width:29px;height:31px;border-radius:2px}
</style>
</head>
<body>
<div class="page">

  <header class="site-header">
    <div class="brand"><i class="brand-mark"></i>Travolia.net</div>
    <div class="account">
      <a class="btn-login" href="#">Login</a>
      <a class="btn-signup" href="#">SignUp</a>
    </div>
    <nav class="main-nav">
      <a class="is-current" href="#">Home</a>
      <a href="#">News</a>
      <a href="#">Search</a>
      <a href="#">Blogs</a>
      <a href="#">Pictures</a>
      <a href="#">Videos</a>
      <a href="#">Events</a>
      <a href="#">Hot or Not</a>
    </nav>
  </header>

  <section class="hero">
    <h1 class="hero-title">Find or serve as a Muse</h1>
    <p class="hero-sub">The dating and networking site for the creative. Single and seeking? Looking to connect with other artists? This is the place for you! <a href="#">JOIN NOW&gt;</a></p>
  </section>

  <div class="photo warm" style="left:438px;top:252px;width:32px;height:153px" role="img" aria-label="Photo of a smiling couple"></div>
  <div class="photo cool" style="left:438px;top:408px;width:32px;height:87px" role="img" aria-label="Photo of a couple outdoors"></div>
  <div class="photo" style="left:474px;top:252px;width:203px;height:101px" role="img" aria-label="Photo of a couple lying together and smiling"></div>
  <div class="photo warm" style="left:474px;top:357px;width:203px;height:138px" role="img" aria-label="Photo of a laughing couple"></div>
  <div class="photo cool" style="left:682px;top:252px;width:134px;height:153px" role="img" aria-label="Photo of a woman hugging a man from behind"></div>
  <div class="photo cool" style="left:682px;top:409px;width:134px;height:86px" role="img" aria-label="Photo of a couple in sunglasses by the sea"></div>
  <div class="photo" style="left:822px;top:252px;width:171px;height:102px" role="img" aria-label="Photo of a smiling couple cheek to cheek"></div>
  <div class="photo warm" style="left:822px;top:358px;width:171px;height:137px" role="img" aria-label="Photo of a couple lying on grass"></div>

  <form class="join">
    <div class="join-head">Join <span>Travolia.net</span> Now!</div>
    <span class="field-label" style="left:12px;top:62px">I'm a</span>
    <div class="box select" style="left:43px;top:59px;width:56px">Man</div>
    <span class="field-label" style="left:110px;top:62px">Seeking a</span>
    <div class="box select" style="left:168px;top:59px;width:57px">Woman</div>
    <span class="field-label" style="left:12px;top:110px">Between ages</span>
    <div class="box select" style="left:91px;top:107px;width:39px">24</div>
    <span class="field-label" style="left:140px;top:110px">and</span>
    <div class="box select" style="left:186px;top:107px;width:39px">43</div>
    <div class="box" style="left:12px;top:156px;width:100px">Enter ZIP Code</div>
    <div class="box select" style="left:124px;top:156px;width:101px">United States</div>
    <div class="box" style="left:12px;top:203px;width:213px">Enter Email ID</div>
    <div class="box" style="left:12px;top:249px;width:213px">Create Your Password</div>
    <div class="btn-match">Find my matches</div>
    <div class="join-foot"></div>
  </form>

  <section class="welcome">
    <h2 class="section-title">Welcome to <span>Travolia.net</span></h2>
    <p>Where heart and art meet....since forever. The dating and networking site for the creative.&nbsp; Single &amp; seeking? Looking to connect with other artists?&nbsp; This is the place for you! Musicians, painters, writers, actors, sculptors, photographers, poets, performance artists, cartoonists, actresses, singers, comics, artisens and more all meet up here. Sometimes a spark is needed to be given or received. Ask Ardel, or Tom Vey, or Orlani. Discover, colloborate, share your passion, make a connection. Find true love or friendship. Find or be a creative inspiration. Muses, Graces and Fates await you here....create a profile today!</p>
    <a class="read-more" href="#">Read more</a>
  </section>
  <div class="divider-v"></div>

  <section class="members">
    <h2 class="section-title">Members</h2>
    <div class="member" style="left:1px;top:36px"><div class="face" role="img" aria-label="Member photo"></div><span>Julie</span></div>
    <div class="member" style="left:65px;top:36px"><div class="face" role="img" aria-label="Member photo"></div><span>Betty</span></div>
    <div class="member" style="left:129px;top:36px"><div class="face" role="img" aria-label="Member photo"></div><span>Andrea</span></div>
    <div class="member" style="left:193px;top:36px"><div class="face" role="img" aria-label="Member photo"></div><span>Alan</span></div>
    <div class="member" style="left:1px;top:120px"><div class="face" role="img" aria-label="Member photo"></div><span>Steven</span></div>
    <div class="member" style="left:65px;top:120px"><div class="face" role="img" aria-label="Member photo"></div><span>David</span></div>
    <div class="member" style="left:129px;top:120px"><div class="face" role="img" aria-label="Member photo"></div><span>Laura</span></div>
    <div class="member" style="left:193px;top:120px"><div class="face" role="img" aria-label="Member photo"></div><span>Nancy</span></div>
  </section>

  <div class="rule" style="top:847px"></div>
  <nav class="footer-nav">
    <a href="#">About Us</a><a href="#">Community</a><a href="#">Resources</a><a href="#">Mobile Apps</a><a href="#">Sitemap</a><a href="#">Privacy &amp; Policy</a><a href="#">Terms of Use</a><a href="#">Testimonials</a><a href="#">Contact Us</a>
  </nav>
  <p class="footer-copy">Lorem ipsum dolor sit amet consectetur adipiscing elit duis, ante dolore magna nisi ante vestibulum ut dolore nisi porta tempor ullalampur sit ut Aliquam ut ante dolore magna nisi, lorem ipsum dolor sit amet consectetur adipiscing elit duis ante dolore. Sed ut parspatisas ante dolore ut amet vestibulum ante dolore. Donec massa lactuis ante dolore morbi quam tortor ut aliquam. Lorem ipsum dolor sit amet consectetur adipiscing elit ante dolore, sed ut parspatuisas ut magna.</p>
  <div class="badge" role="img" aria-label="Accreditation badge"></div>
  <div class="rule" style="top:1000px"></div>

  <div class="footer-brand"><i></i>Travolia.net</div>
  <p class="copyright">Copyright © 2013 travolia.net</p>
  <div class="social" style="left:883px"><span style="background:#1d55b5" role="img" aria-label="Social link"></span></div>
  <div class="social" style="left:923px"><span style="background:#3cb2e6" role="img" aria-label="Social link"></span></div>
  <div class="social" style="left:964px"><span style="background:#f5b20f" role="img" aria-label="Feed link"></span></div>

</div>
</body>
</html>
```